Craft oriented film company needs a Business Card design

Hi all,
We're a 2-man band film company in New Zealand called Harrow Pictures. We're good honest blokes, who are very passionate about the craft of film making. I've attached our current logo which has a bit of a crafty/artisan feel that we like. Feel free to use it - or throw the baby out with the bathwater and start again..... you never know, you might inspire a complete brand re-work.

In any case, the vibe we want to give out is that we are solid, dependable and no bullshit - but without compromising creative excellence and being in the now. We like the 'Brooklyn' artisan style of work.

Preferably single sided.

We need the standard stuff:
Name, job title, cellphone, email address and physical address (this can be smaller if you like - street, suburb, city & zip, country [if you want])

Check out our website to learn more about us: harrowpictures.example

Target Market(s)

Brand marketers and advertising agency creatives looking for video production.

Industry/Entity Type

Baby

Requirements
Should not have
• Nothing flashy or too 'futuristic', we want it to feel grounded and real. A limited colour palette is preferred.
We don't want any film reels or cameras or anything obvious like that.

```html
<!DOCTYPE html>
<html lang="en">
<head>
<meta charset="utf-8">
<title>Harrow Pictures – Business Card</title>
<link rel="stylesheet" href="https://fonts.googleapis.com/css2?family=Arimo:wght@400;700&display=swap">
<style>
  :root {
    --backdrop: #9b774c;
    --card: #ffffff;
    --ink: #4a4a4a;
    --ink-strong: #3f3f3f;
    --brand: #111111;
    --rule: #c9c9c9;
  }
  * { margin: 0; padding: 0; box-sizing: border-box; }
  html, body {
    width: 1200px;
    height: 755px;
    overflow: hidden;
  }
  body {
    background: var(--backdrop);
    font-family: "Arimo", Arial, sans-serif;
    color: var(--ink);
    position: relative;
  }
  .card {
    position: absolute;
    left: 96px;
    top: 86px;
    width: 1008px;
    height: 576px;
    background: var(--card);
  }
  .brand {
    position: absolute;
    left: 0;
    right: 0;
    top: 130px;
    display: flex;
    align-items: center;
    justify-content: center;
    gap: 18px;
  }
  .brand-dot {
    width: 34px;
    height: 34px;
    border-radius: 50%;
    background: var(--brand);
  }
  .brand-name {
    font-weight: 700;
    font-size: 46px;
    color: var(--brand);
    letter-spacing: 1px;
  }
  .identity {
    position: absolute;
    right: 561px;
    top: 362px;
    text-align: right;
  }
  .identity .person {
    font-weight: 700;
    font-size: 38px;
    color: var(--ink-strong);
    line-height: 1;
  }
  .identity .role {
    font-size: 24px;
    margin-top: 16px;
    line-height: 1;
  }
  .identity .address {
    font-size: 24px;
    line-height: 32px;
    margin-top: 16px;
  }
  .divider {
    position: absolute;
    left: 472px;
    top: 374px;
    width: 3px;
    height: 150px;
    background: linear-gradient(to bottom, transparent, var(--rule) 20%, var(--rule) 80%, transparent);
  }
  .contacts {
    position: absolute;
    left: 497px;
    top: 372px;
    list-style: none;
  }
  .contacts li {
    display: flex;
    align-items: center;
    gap: 10px;
    height: 56px;
    font-size: 26px;
  }
  .contacts svg {
    width: 20px;
    height: 22px;
    fill: var(--ink);
    flex: none;
  }
</style>
</head>
<body>
  <section class="card">
    <div class="brand">
      <span class="brand-dot"></span>
      <span class="brand-name">Harrow Pictures</span>
    </div>

    <div class="identity">
      <p class="person">Your Name</p>
      <p class="role">Title</p>
      <p class="address">street, suburb, city<br>zip, country</p>
    </div>

    <div class="divider"></div>

    <ul class="contacts">
      <li>
        <svg viewBox="0 0 20 22" aria-hidden="true"><path d="M6 1h8a2 2 0 0 1 2 2v16a2 2 0 0 1-2 2H6a2 2 0 0 1-2-2V3a2 2 0 0 1 2-2zm0 3v10h8V4zm4 12.5a1.5 1.5 0 1 0 0 3 1.5 1.5 0 0 0 0-3z"/></svg>
        <span>(123) 456-7890</span>
      </li>
      <li>
        <svg viewBox="0 0 20 22" aria-hidden="true"><path d="M1 6l9 6 9-6v11H1zm0-2h18l-9 6z"/></svg>
        <span>Info@harrowpictures.example</span>
      </li>
      <li>
        <svg viewBox="0 0 20 22" aria-hidden="true"><path d="M10 2a9 9 0 1 0 0 18 9 9 0 0 0 0-18zm0 2c1 0 2.3 2 2.6 5H7.4C7.7 6 9 4 10 4zm-2.6 7h5.2c-.3 3-1.6 5-2.6 5s-2.3-2-2.6-5zM3.1 9A7 7 0 0 1 6.8 4.8 11 11 0 0 0 5.4 9zm0 2h2.3a11 11 0 0 0 1.4 4.2A7 7 0 0 1 3.1 11zm11.5 0h2.3a7 7 0 0 1-3.7 4.2 11 11 0 0 0 1.4-4.2zm0-2a11 11 0 0 0-1.4-4.2A7 7 0 0 1 16.9 9z"/></svg>
        <span>www.harrowpictures.example</span>
      </li>
    </ul>
  </section>
</body>
</html>
```